Business Card design for an International Import Export House

We need a Business Card design for our import export business. We trade in Minerals, Metals, Rice, Sugar, Steel etc.. The design should be minimalistic. It may or may not contain the physical address. In case you want to include the physical address - 418 Verandah Heights, Marlow Sector 9, Ardenpur, Westmark, India, 480213.

Target Market(s)

Steel Mills or Steel Plants, Factories, Mining businesses, Industrial houses, Government Agencies

Industry/Entity Type

Importer

Contact Information for Business Card

Business Name - Corvane Overseas

Font styles to use
Other font styles liked:
• montserrat

Requirements
Must have
• Ravi Kandola - President
• www.corvaneoverseas.com
• ravi@corvaneoverseas.com
• +91-987-654-3217
Nice to have
• worldwide suppliers of ores

```html
<!DOCTYPE html>
<html lang="en">
<head>
<meta charset="UTF-8">
<title>Corvane Overseas — Business Card</title>
<link href="https://fonts.googleapis.com/css2?family=Montserrat:wght@400;500;700&display=swap" rel="stylesheet">
<style>
  :root {
    --teal: #3e8fab;
    --teal-light: #4a9cb7;
    --teal-deep: #2f7893;
    --ink: #1b1f22;
    --grey-block: #e6e6e6;
    --paper: #ffffff;
    --text-dark: #222629;
    --text-mid: #3a3f43;
    --backdrop: #2b2d2f;
  }
  * { margin: 0; padding: 0; box-sizing: border-box; }
  html, body {
    width: 1200px; height: 1000px; overflow: hidden;
    background: var(--backdrop);
    font-family: "Montserrat", sans-serif;
  }
  .card {
    position: absolute;
    width: 720px; height: 410px;
    left: 240px;
    background: var(--paper);
    border-radius: 36px;
    overflow: hidden;
  }
  .card--front { top: 60px; }
  .card--back { top: 530px; }

  /* Brand lockup */
  .brand {
    position: absolute;
    display: flex; align-items: center; gap: 14px;
  }
  .brand__dot {
    border-radius: 50%;
    background: var(--teal);
    flex-shrink: 0;
  }
  .brand__name {
    font-weight: 700;
    color: var(--teal);
    letter-spacing: 0.5px;
    white-space: nowrap;
  }
  .card--front .brand { left: 0; right: 0; top: 110px; justify-content: center; }
  .card--front .brand__dot { width: 46px; height: 46px; }
  .card--front .brand__name { font-size: 34px; }
  .card--back .brand { right: 48px; top: 52px; }
  .card--back .brand__dot { width: 30px; height: 30px; }
  .card--back .brand__name { font-size: 24px; }

  /* Colour band */
  .band {
    position: absolute; left: 0; right: 0;
    display: flex; height: 50px;
  }
  .band__main {
    flex: 1;
    min-width: 0;
    background: linear-gradient(90deg, var(--teal-light), var(--teal));
    display: flex; align-items: center;
    color: var(--paper);
    white-space: nowrap;
  }
  .band__accent { width: 56px; background: var(--teal-deep); }
  .band__light { width: 40px; background: var(--grey-block); }
  .band__dark { width: 64px; background: var(--ink); }

  .card--front .band { top: 290px; }
  .card--front .band__main { padding-left: 180px; font-size: 16px; letter-spacing: 4px; font-weight: 400; }
  .card--front .foot-strip {
    position: absolute; left: 0; bottom: 0;
    width: 260px; height: 24px; background: var(--teal);
  }

  .card--back .band { bottom: 0; height: 54px; }
  .card--back .band__main { padding-left: 20px; gap: 12px; font-size: 12px; }
  .card--back .band__accent { width: 40px; }
  .card--back .band__light { width: 30px; }
  .card--back .band__dark { width: 50px; }
  .pin-badge {
    width: 32px; height: 32px; border-radius: 50%;
    background: var(--paper);
    display: flex; align-items: center; justify-content: center;
    flex-shrink: 0;
  }

  /* Identity */
  .identity { position: absolute; left: 110px; top: 150px; }
  .identity__name {
    font-size: 26px; font-weight: 700; color: var(--text-dark);
    letter-spacing: 0.5px;
  }
  .identity__name span { color: var(--teal); font-weight: 500; }
  .identity__role {
    font-size: 20px; font-weight: 400; color: var(--text-mid);
    letter-spacing: 1px; margin-top: 2px;
  }
  .identity__rule {
    position: absolute; left: 0; top: 190px;
    width: 100px; height: 2px; background: var(--teal);
  }

  /* Contacts */
  .contacts { position: absolute; left: 60px; top: 250px; }
  .contact {
    display: flex; align-items: center; gap: 18px;
    margin-bottom: 14px;
  }
  .contact__icon {
    width: 32px; height: 32px; border-radius: 50%;
    display: flex; align-items: center; justify-content: center;
    flex-shrink: 0;
  }
  .contact__icon--ring { border: 2px solid var(--teal); }
  .contact__icon--solid { background: var(--teal-deep); }
  .contact__text { font-size: 15px; color: var(--text-dark); line-height: 1.3; white-space: nowrap; }
</style>
</head>
<body>

<section class="card card--front" aria-label="Card front">
  <div class="brand">
    <span class="brand__dot"></span>
    <span class="brand__name">CORVANE OVERSEAS</span>
  </div>
  <div class="band">
    <div class="band__main">WWW.CORVANEOVERSEAS.COM</div>
    <div class="band__accent"></div>
    <div class="band__light"></div>
    <div class="band__dark"></div>
  </div>
  <div class="foot-strip"></div>
</section>

<section class="card card--back" aria-label="Card back">
  <div class="brand">
    <span class="brand__dot"></span>
    <span class="brand__name">CORVANE OVERSEAS</span>
  </div>

  <div class="identity__rule"></div>
  <div class="identity">
    <p class="identity__name">RAVI <span>KANDOLA</span></p>
    <p class="identity__role">PRESIDENT</p>
  </div>

  <div class="contacts">
    <div class="contact">
      <span class="contact__icon contact__icon--ring">
        <svg width="16" height="16" viewBox="0 0 24 24" aria-hidden="true">
          <path d="M6.6 10.8a15 15 0 0 0 6.6 6.6l2.2-2.2a1 1 0 0 1 1-.25 11.4 11.4 0 0 0 3.6.57 1 1 0 0 1 1 1V20a1 1 0 0 1-1 1A17 17 0 0 1 3 4a1 1 0 0 1 1-1h3.5a1 1 0 0 1 1 1c0 1.25.2 2.45.57 3.6a1 1 0 0 1-.25 1z" fill="#3e8fab"/>
        </svg>
      </span>
      <span class="contact__text">+91-987-654-3217</span>
    </div>
    <div class="contact">
      <span class="contact__icon contact__icon--solid">
        <svg width="18" height="18" viewBox="0 0 24 24" aria-hidden="true" fill="none" stroke="#fff" stroke-width="1.6">
          <circle cx="12" cy="12" r="9"/>
          <ellipse cx="12" cy="12" rx="4" ry="9"/>
          <line x1="3" y1="12" x2="21" y2="12"/>
          <line x1="4.5" y1="7.5" x2="19.5" y2="7.5"/>
          <line x1="4.5" y1="16.5" x2="19.5" y2="16.5"/>
        </svg>
      </span>
      <span class="contact__text">ravi@corvaneoverseas.com<br>www.corvaneoverseas.com</span>
    </div>
  </div>

  <div class="band">
    <div class="band__main">
      <span class="pin-badge">
        <svg width="16" height="18" viewBox="0 0 24 24" aria-hidden="true">
          <path d="M12 2a7 7 0 0 0-7 7c0 5 7 13 7 13s7-8 7-13a7 7 0 0 0-7-7zm0 9.5A2.5 2.5 0 1 1 12 6.5a2.5 2.5 0 0 1 0 5z" fill="#3e8fab"/>
        </svg>
      </span>
      <span>418 Verandah Heights, Marlow Sector 9, Ardenpur, Westmark, India, 480213.</span>
    </div>
    <div class="band__accent"></div>
    <div class="band__light"></div>
    <div class="band__dark"></div>
  </div>
</section>

</body>
</html>
```